Business card design and logo needed

We have been operating as Ridgeline Posts for 30 years but never had a logo and feel there is a need for one, but have no idea for a design.
We specialise in all types of rural fencing including post and wire, post and rail, electric, chainmesh and to a lesser extent, also do industrial security fencing.
Updates

Sorry, but website is ridgelineposts.example

No .au on the end!
My apologies

Regards, Darren

Target Market(s)

Rural/acreage property owners, particularly horse people.

Industry/Entity Type

Industrial

Contact Information for Business Card

Ridgeline Posts Darren Kellett 0499 572106. Lewis Kellett 0499 613720
Email: ridgelineposts@mailhub.example
Website: www.ridgelineposts.example.au

Requirements
Must have
• Would like to highlight website address - use the business card to advertise the website or to push them to check it out.

```html
<!DOCTYPE html>
<html lang="en">
<head>
<meta charset="utf-8">
<title>Ridgeline Posts – Business Card</title>
<link rel="stylesheet" href="https://fonts.googleapis.com/css2?family=Source+Sans+3:wght@400;600;700&display=swap">
<style>
  :root {
    --page: #ffffff;
    --card: #d6dc3a;
    --brand-red: #8e2a1c;
    --accent-orange: #e0801e;
    --name-brown: #7a2818;
    --mark-dark: #3b2b24;
    --label: #000000;
    --shadow: rgba(0, 0, 0, 0.45);
  }
  * { margin: 0; padding: 0; box-sizing: border-box; }
  html, body {
    width: 1200px;
    height: 800px;
    overflow: hidden;
    background: var(--page);
    font-family: "Source Sans 3", "Myriad Pro", Arial, sans-serif;
  }
  .sheet { position: relative; width: 1200px; height: 800px; }

  .side-label {
    position: absolute;
    font-size: 38px;
    font-weight: 600;
    color: var(--label);
    line-height: 1;
  }
  .side-label--front { left: 773px; top: 84px; }
  .side-label--back { left: 346px; top: 704px; }

  .card {
    position: absolute;
    background: var(--card);
    box-shadow: 2px 3px 4px var(--shadow);
  }
  .card--front { left: 201px; top: 89px; width: 546px; height: 314px; }
  .card--back { left: 466px; top: 432px; width: 531px; height: 305px; }

  .brand {
    position: absolute;
    left: 144px;
    top: 182px;
    display: flex;
    align-items: center;
    gap: 14px;
  }
  .brand__name {
    font-size: 36px;
    font-weight: 700;
    text-transform: uppercase;
    letter-spacing: -0.5px;
    color: var(--brand-red);
    line-height: 1;
  }
  .brand__square {
    width: 34px;
    height: 34px;
    background: var(--mark-dark);
  }
  .website {
    position: absolute;
    left: 147px;
    top: 227px;
    font-size: 19px;
    font-weight: 700;
    color: var(--accent-orange);
  }

  .contacts {
    position: absolute;
    left: 265px;
    top: 180px;
  }
  .contact {
    display: flex;
    align-items: baseline;
    height: 27px;
  }
  .contact__name {
    font-size: 19px;
    font-weight: 700;
    color: var(--name-brown);
    width: 118px;
  }
  .contact__sep {
    font-size: 14px;
    font-weight: 700;
    color: var(--accent-orange);
    margin-right: 7px;
  }
  .contact__phone {
    font-size: 14.5px;
    color: var(--name-brown);
  }
  .email {
    margin-top: 6px;
    font-size: 15px;
    color: var(--accent-orange);
  }
</style>
</head>
<body>
<main class="sheet">
  <section class="card card--front" aria-label="Card front">
    <div class="brand">
      <span class="brand__name">Ridgeline Posts</span>
      <span class="brand__square" aria-hidden="true"></span>
    </div>
    <p class="website">www.ridgelineposts.example</p>
  </section>
  <p class="side-label side-label--front">Front</p>

  <section class="card card--back" aria-label="Card back">
    <div class="contacts">
      <p class="contact">
        <span class="contact__name">Darren Kellett</span>
        <span class="contact__sep">::</span>
        <span class="contact__phone">0499 572106</span>
      </p>
      <p class="contact">
        <span class="contact__name">Lewis Kellett</span>
        <span class="contact__sep">::</span>
        <span class="contact__phone">0499 613720</span>
      </p>
      <p class="email">ridgelineposts@mailhub.example</p>
    </div>
  </section>
  <p class="side-label side-label--back">Back</p>
</main>
</body>
</html>
```